Stationary Design

Harbor Stagecraft Works, Inc
27450 Lindell Ave Ste 3, Cedar Bluff, CA 90418
Office: 213-555-0187 Email: admin@hswinc.example

Industry/Entity Type

Entertainment

Colors
0054AA
0677BA
7BADD7
CADEEF
E8F1F8

```html
<!DOCTYPE html>
<html lang="en">
<head>
<meta charset="utf-8">
<title>Harbor Stagecraft Works – Business Card</title>
<link rel="stylesheet" href="https://fonts.googleapis.com/css2?family=Open+Sans:wght@400;600&family=Arimo:wght@400&display=swap">
<style>
  :root {
    --blue-deep: #0054AA;
    --blue-mid: #0677BA;
    --blue-soft: #7BADD7;
    --blue-pale: #CADEEF;
    --blue-mist: #E8F1F8;
    --cyan-foil: #3FC6F0;
    --ink: #3a3a3a;
    --ink-light: #777;
    --rule: #c9c9c9;
    --strip-grey: #a9a9a9;
    --backdrop: #e4e6e9;
    --card-white: #ffffff;
  }
  * { margin: 0; padding: 0; box-sizing: border-box; }
  html, body {
    width: 1200px; height: 874px; overflow: hidden;
    background: var(--backdrop);
  }
  .canvas {
    position: relative; width: 1200px; height: 874px;
    display: flex; flex-direction: column; align-items: center; justify-content: center;
    gap: 40px;
  }
  .card {
    position: relative; width: 620px; height: 354px;
    border-radius: 16px; overflow: hidden;
    box-shadow: 0 6px 18px rgba(0,0,0,0.12);
  }

  /* Back side */
  .card-back {
    background: var(--blue-deep);
    display: flex; align-items: center; justify-content: center; gap: 16px;
  }
  .brand-mark {
    width: 54px; height: 54px; border-radius: 50%;
    border: 5px solid var(--cyan-foil);
    flex: none;
  }
  .brand-name {
    font-family: "Open Sans", sans-serif; font-weight: 600;
    letter-spacing: 1px; text-transform: uppercase; white-space: nowrap;
  }
  .card-back .brand-name { color: var(--cyan-foil); font-size: 28px; }

  /* Front side */
  .card-front { background: var(--card-white); }
  .front-brand {
    position: absolute; top: 92px; right: 48px;
    display: flex; align-items: center; gap: 12px;
  }
  .front-brand .brand-mark { width: 40px; height: 40px; border-width: 4px; border-color: var(--blue-deep); }
  .front-brand .brand-name { color: var(--blue-deep); font-size: 19px; }

  .holder { position: absolute; left: 44px; top: 158px; font-family: "Open Sans", sans-serif; }
  .holder-name { color: var(--blue-deep); font-size: 30px; font-weight: 600; line-height: 1.05; }
  .holder-title { color: var(--ink-light); font-size: 14px; }

  .address {
    position: absolute; left: 44px; top: 222px;
    font-family: "Arimo", sans-serif; font-size: 15px; line-height: 1.3; color: var(--ink);
    font-style: normal;
  }
  .divider {
    position: absolute; left: 44px; right: 40px; top: 290px;
    height: 1px; background: var(--rule);
  }
  .contact {
    position: absolute; right: 40px; top: 240px;
    font-family: "Arimo", sans-serif; font-size: 15px; color: var(--ink);
    text-align: right; line-height: 1.45;
  }
  .contact-line { display: flex; align-items: center; justify-content: flex-end; gap: 8px; }
  .contact-line svg { width: 14px; height: 14px; fill: var(--blue-deep); }

  .footer-band { position: absolute; left: 0; bottom: 0; width: 620px; height: 46px; }
  .website {
    position: absolute; right: 40px; bottom: 10px;
    font-family: "Arimo", sans-serif; font-size: 15px; color: var(--card-white);
  }
</style>
</head>
<body>
<main class="canvas">

  <section class="card card-back" aria-label="Card back">
    <span class="brand-mark"></span>
    <span class="brand-name">Harbor Stagecraft Works</span>
  </section>

  <section class="card card-front" aria-label="Card front">
    <div class="front-brand">
      <span class="brand-mark"></span>
      <span class="brand-name">Harbor Stagecraft Works</span>
    </div>

    <div class="holder">
      <p class="holder-name">Daniel Reyes</p>
      <p class="holder-title">President</p>
    </div>

    <address class="address">
      Harbor Stagecraft Works, Inc<br>
      27450 Lindell Ave Ste 3,<br>
      Cedar Bluff, CA 90418
    </address>

    <div class="contact">
      <p class="contact-line">213-555-0187
        <svg viewBox="0 0 24 24" aria-hidden="true"><path d="M6.6 10.8a15 15 0 0 0 6.6 6.6l2.2-2.2c.3-.3.7-.4 1-.2 1.1.4 2.3.6 3.6.6.6 0 1 .4 1 1V20c0 .6-.4 1-1 1A17 17 0 0 1 3 4c0-.6.4-1 1-1h3.5c.6 0 1 .4 1 1 0 1.3.2 2.5.6 3.6.1.3 0 .7-.2 1z"/></svg>
      </p>
      <p class="contact-line">admin@hswinc.example
        <svg viewBox="0 0 24 24" aria-hidden="true"><path d="M2 5h20v14H2zM3.5 6.5 12 13l8.5-6.5z" fill-rule="evenodd"/></svg>
      </p>
    </div>

    <div class="divider"></div>

    <svg class="footer-band" viewBox="0 0 620 46" aria-hidden="true">
      <polygon points="0,34 300,34 296,46 0,46" fill="var(--strip-grey)"/>
      <polygon points="330,0 620,0 620,46 300,46" fill="var(--blue-deep)"/>
    </svg>
    <p class="website">www.hswinc.example</p>
  </section>

</main>
</body>
</html>
```